Arizona Pool Company Brochure

**** UPDATE 2-8-2014 ****

Size should be 11" X 17" or larger (tri or bi fold).

We're going to let the contest run it's full duration to allow for more time spent on designs.

No black backgrounds.

Consideration should be given to having the text be easy to read and in a nice, organized format.

*****************************

We're looking for an eye-catching, colorful brochure that will explain what we do, who we are... and what sets us apart from the competition.

Our company provides swimming pool service, repair, and custom renovations throughout the Phoenix, Arizona metropolitan area. These brochures will be hand-delivered to each prospective customer we visit.

The brochure will include images of our work, product logos, and a unique design that separates our company apart from the rest.

The brochure should be tri-fold. Although, if a designer wants to (or has better ideas) for a different lay-out, then we're open to seeing what can be done.

Colors we like: Blue, White, Silver, Copper, Green (accent color)

We like designs that are unique/different. Professional. Creative. Sleek. Sexy. Custom. We don't want the brochure to be "pretentious". We'd like for these brochures to leave a lasting impression with our prospective clients... and hopefully earn us more business.

We don't want the brochure to be too wordy, however if the designer feels we need to cut back (or add), let us know.

Our motto is "Every Wave Stays Bright".

You can view some of our projects, and what we're about either at our website (tidewellaqua.com), Chatterbook (www.facebook/tidewellaqua), or Searchly+ (https://plus.google.com/+Tidewellaqua). Thank you!

- Print-

(Front) Logo

Service - Repair - Renovation
480-555-0147
tidewellaqua.com
service@tidewellaqua.com
Like Us On Chatterbook! Chatterbook LOGO
Searchly Circle LOGO

(Body) Why Choose Us?

Thank you for the opportunity for our company to become your pool service provider!

We’re committed to providing the best customer service possible! At the end of the day you want your pool to be clean, clear, operational, and for your service provider to be available when you need them!

We’re licensed with the Desert State Builders Licensing Office, Bonded, and Fully Insured.
A+ reviews with the Fair Trade Merchants Council, Marlo's Roster, Vetchly, Ornu, Chatterbook, and Searchly!
All technicians are employees... not sub-contractors! Our employees are hard working, dependable, professional, and expected to follow our strict protocol for servicing your pool.
Flat-fee service rates! Any additional equipment repairs, maintenance, or chemical implementations are directly authorized by you!
No contracts! Our Service Level Agreement Form allows you to select your desired level of authorization for equipment repairs, filter maintenance, and extra chemical implementation programs.
Our uniformed technicians arrive in distinctive, clean GPS-tracked company trucks.
We leave detailed service slips after each service visit. In addition, all service visit information is electronically recorded and stored.
Easy, online account management to view and pay invoices or authorize estimates.
Invoices, estimates, questions, pictures, and video are communicated via e-mail!
Free service calls to diagnose equipment issues outside of our normal service.
10% Service Client Discount for all repairs and replacement items.
Tidewell Aqua Service knows the importance of communication! We’re available by phone, email, or text all days of the week.

(Body) Our Methodology

We believe in 5 important factors in maintaining a clean, clear, and operational pool...

Good, Clean Water! Our local water supply contains high amounts of minerals. Pool chemicals add to this problem in a short amount of time. Our philosophy is to use the least amount of chemicals possible to achieve optimal water balance.
Efficient Water Flow! The invention of variable-speed pumps has enabled the ability to "dial in" proper water flow... while driving down energy costs.
Proper Filtration! Today’s high-capacity cartridge filters provide great filtration, save on wasted water from backwashing sand filters, and eliminate the need for water flow-restricting backwash valves.
Functioning Cleaning System! Having a working automatic cleaning system is vital in keeping the pool surface clean of debris and dirt... and free of staining.
A Dependable And Professional Pool Maintenance Technician! Our job is to not only oversee all of the items listed above... but to make sure your pool is in the best condition possible!

(Body) Equipment Repair & Installation

We’re educated on all phases of swimming pool equipment repair and installation... with a focus on energy-efficiency and optimum performance!

We’re an KVE & BTU Authorized Installer of variable-speed pool pumps. KVE & BTU trust us to properly install and calibrate all variable-speed pumps. We've been equipped to handle the new industry standards on variable-speed pumps since Arizona law went into effect January 1st, 2011.
We’re experts at acid washes and erasing the mineral build-up off of waterlines. All work is done in-house with our customized cleaning rig and trailer.
Heating systems. New efficiency standards have made installation and operation more affordable than ever.
Remote control automation systems. Technology now allows the user to easily view and control their entire pool system via a remote home computer, tablet, or phone!
Brilliant, color-changing LED lighting for pools and spas! The benefits of LED include brighter and broader displays... while lasting much longer than your typical light bulbs.
Salt systems provide a soft-water experience! In addition to the benefit of better feeling water, salt systems generate plenty of chlorine to keep your pool sanitized.

(Body) About Us

A native to Phoenix, Darren Whitcombe founded Tidewell Aqua Service in 2000. Our company was built from the ground up by way of hard work, word of mouth, and determination. Our company will always remain firmly grounded, and continue to develop systems that put our customers first!

Our philosophy is to treat every pool as if it were our own, run an efficient and organized business, and care for our employees.

Tidewell Aqua Service is a yearly, proud contributor to the Saguaro Youth Medical Center Splash Smart Day. Please educate and watch all children around water... every accident can be avoided.

(Back) Contact Us
Logos To Use, Files Uploaded: Marlo's Roster, FTMC, Quorvix, Searchly+, Chatterbook, KVE/BTU logo, Saguaro Youth Medical Center

Office: 480-555-0147 | Fax: 480-555-0193 | Email: service@tidewellaqua.com
tidewellaqua.com

Office / Warehouse Location
41762 East Kettle Lane, Suite 7
Phoenix, Arizona 85000
(NW of Kettle Lane & Mesquite Ridge Drive)

AZ ROC: 731402, 731403, 731404, 605218

Target Market(s)

We target a market of pool owners, which typically have more disposable income.

30 - 75 years old.

Our clients range from first-time home buyers, self-employed, business professionals, doctors, landlords, thousandaires, millionaires.

Industry/Entity Type

Pool Service

Font styles to use
Serif

Colors
0355a3
cfdfed
ffffff
3176b5
eaf1f7

Requirements
Must have
• Must use provided images. We've included a few pool pictures, and will let you decide which ones to incorporate throughout the brochure.

Logos Used:
Tidewell Aqua Service
Quorvix
FTMC
Marlo's Roster
KVE
BTU
Saguaro Youth Medical Center
Searchly+
Chatterbook

Image pic of some of our trucks.

Nice to have
• Equipment images worked in.
Should not have
• Cartoonish fonts or design. No "Love" hearts!!

```html
<!DOCTYPE html>
<html lang="en">
<head>
<meta charset="utf-8">
<title>Tidewell Aqua Service Brochure</title>
<link href="https://fonts.googleapis.com/css2?family=Open+Sans:wght@400;600;700&family=Raleway:wght@200;300;400;600&display=swap" rel="stylesheet">
<style>
:root{
  --brand-blue:#0355a3;
  --mid-blue:#3176b5;
  --steel:#5f82b0;
  --steel-dark:#4a6e9f;
  --ice:#cfdfed;
  --mist:#eaf1f7;
  --white:#ffffff;
  --green:#6cb33f;
  --lime:#7bbf2a;
  --red:#e8303a;
  --ink:#4a4a4a;
  --bar:#3b3d40;
}
*{box-sizing:border-box;margin:0;padding:0}
html,body{width:799px;height:1200px;overflow:hidden;background:var(--white)}
body{position:relative;font-family:"Open Sans",Arial,sans-serif;color:var(--ink)}
.spread{position:absolute;overflow:hidden}
.spread--outside{left:11px;top:11px;width:784px;height:552px}
.spread--inside{left:0;top:637px;width:799px;height:563px}
.panel{position:absolute;top:0;height:100%;overflow:hidden}
.photo{position:absolute}

/* shared */
.ticks{list-style:none}
.ticks li{position:relative;padding-left:16px;margin-bottom:6px;font-size:6.6px;line-height:1.32}
.ticks li::before{content:"";position:absolute;left:3px;top:1px;width:4px;height:7px;border-right:2px solid var(--green);border-bottom:2px solid var(--green);transform:rotate(40deg)}
.brand{display:flex;align-items:center;gap:5px}
.brand__dot{border-radius:50%;background:var(--brand-blue);flex:none}
.brand__name{font-family:"Open Sans",Arial,sans-serif;font-weight:700;color:var(--brand-blue);letter-spacing:-.3px}
.brand__tag{font-family:"Open Sans",Arial,sans-serif;font-weight:700;color:var(--brand-blue);font-size:7.5px;margin-top:1px;white-space:nowrap}

/* why choose us */
.panel--why{left:0;width:252px;background:var(--white)}
.why__photo{left:0;top:0;width:252px;height:462px;background:linear-gradient(180deg,#c9cfd2 0%,#9fa79a 45%,#6f8a90 70%,#a6896c 100%)}
.why__card{position:absolute;left:0;top:0;width:240px;height:462px;background:rgba(255,255,255,.86)}
.why__title{position:absolute;left:-168px;top:200px;width:390px;transform:rotate(-90deg);font-family:Raleway,sans-serif;font-weight:200;font-size:38px;letter-spacing:1px;color:#555;white-space:nowrap}
.why__title b{font-weight:400;color:var(--red)}
.why__intro{position:absolute;left:63px;top:4px;width:172px;font-size:6.6px;line-height:1.34}
.why__list{position:absolute;left:50px;top:66px;width:188px}
.why__list li{margin-bottom:5.4px}
.partners{position:absolute;left:12px;top:440px;width:226px;display:flex;justify-content:space-between;align-items:center}
.partner{display:block}
.partner--a{width:44px;height:13px;border-radius:7px;background:var(--mid-blue)}
.partner--b{width:46px;height:13px;background:var(--red)}
.partner--c{width:20px;height:20px;border-radius:50%;background:var(--green)}
.partner--d{width:40px;height:13px;background:var(--brand-blue)}
.why__foot{position:absolute;left:0;top:462px;width:252px;height:90px;background:linear-gradient(180deg,#f5f7fa,#e3eaf2)}
.why__foot::before{content:"";position:absolute;left:0;top:0;width:100%;height:4px;background:var(--steel)}
.why__foot .brand{position:absolute;left:62px;top:32px}

/* cover middle */
.panel--cover-mid{left:252px;width:266px;background:var(--steel)}
.panel--cover-mid svg{position:absolute;left:0;top:0}
.mid__brand{position:absolute;left:30px;top:410px}
.office{position:absolute;left:26px;top:468px;width:214px;font-size:6.2px;color:#333}
.office__row{display:grid;grid-template-columns:auto 1fr;column-gap:6px}
.office__row strong{font-weight:700;letter-spacing:.3px}
.office__city{color:var(--mid-blue);text-align:center;margin:2px 0 10px 100px}
.office__grid{display:grid;grid-template-columns:32px 64px 38px 64px;row-gap:1px}
.office__grid b{font-weight:700}
.office__grid span{color:var(--mid-blue);white-space:nowrap}
.office__web{text-align:center;margin-top:7px}

/* cover front */
.panel--front{left:518px;width:266px;background:var(--white)}
.front__people{left:0;top:0;width:266px;height:182px;background:radial-gradient(ellipse at 55% 55%,#f1dcc8 0%,#e9eef4 55%,#ffffff 85%)}
.front__brand{position:absolute;left:26px;top:190px}
.front__brand .brand__name{font-size:25px}
.front__brand .brand__dot{width:26px;height:26px}
.front__brand .brand__tag{font-size:9px}
.front__tagline{position:absolute;left:0;top:263px;width:266px;text-align:center;font-family:Raleway,sans-serif;font-weight:600;font-size:13.5px;color:var(--lime);letter-spacing:.2px}
.front__pool{left:0;top:292px;width:266px;height:230px;background:linear-gradient(180deg,#ffffff 0%,#c8d6c4 18%,#8a9a76 38%,#b39a7c 55%,#3f8cb6 75%,#2a6f9a 100%)}
.front__bar{position:absolute;left:0;top:522px;width:266px;height:30px;background:var(--bar);color:#e8e8e8;font-size:7px;padding:5px 8px;display:flex;justify-content:space-between}
.front__bar p{line-height:1.35}
.social{display:flex;align-items:center;gap:3px}
.social i{width:6px;height:6px;background:#8a8f96;display:inline-block}

/* inside left */
.panel--about{left:0;width:265px;height:530px;background:linear-gradient(180deg,var(--steel-dark) 0%,#6686b4 45%,var(--steel) 100%);color:var(--white)}
.section-title{font-family:Raleway,sans-serif;font-weight:300;font-size:25px;color:var(--ice)}
.section-title b{font-weight:300;color:var(--white)}
.about__title{position:absolute;left:20px;top:30px}
.about__text{position:absolute;left:20px;top:66px;width:230px;font-size:6.5px;line-height:1.34}
.about__text p{margin-bottom:6px}
.snap{position:absolute;border:3px solid var(--white);box-shadow:0 2px 4px rgba(0,0,0,.3)}
.snap--a{left:40px;top:170px;width:78px;height:70px;transform:rotate(-8deg);background:linear-gradient(160deg,#8fb4cc,#3d7ea8 55%,#cbb89a)}
.snap--b{left:112px;top:162px;width:98px;height:72px;transform:rotate(6deg);background:linear-gradient(180deg,#b9cfe0,#9c9a8a 45%,#4e95bd)}
.method__title{position:absolute;left:20px;top:276px}
.method__lead{position:absolute;left:36px;top:312px;width:214px;font-size:6.5px;line-height:1.34}
.method__list{position:absolute;left:20px;top:336px;width:232px}
.method__list li{margin-bottom:7px}

/* inside right */
.panel--repair{left:265px;width:534px;height:530px;background:linear-gradient(180deg,#eaf1f7 0%,var(--ice) 100%)}
.repair__hero{left:0;top:0;width:534px;height:215px;background:linear-gradient(180deg,#bcd3e0 0%,#6f8f58 30%,#9a8570 52%,#2f86b3 78%,#cfc0a5 100%)}
.snap--c{left:8px;top:168px;width:148px;height:110px;transform:rotate(-5deg);background:linear-gradient(180deg,#c9d9e4,#8f9a7e 40%,#3c8bb5 75%,#c3ad8e)}
.snap--d{left:150px;top:148px;width:144px;height:112px;transform:rotate(2deg);background:linear-gradient(180deg,#9fb4c2,#8b6f55 40%,#2f79a8 80%)}
.snap--e{left:292px;top:136px;width:172px;height:98px;transform:rotate(-3deg);background:linear-gradient(180deg,#d4e2ec,#7fa06a 35%,#3fa1c8 70%,#c8b79c)}
.repair__title{position:absolute;left:-92px;top:340px;width:260px;transform:rotate(-90deg);font-family:Raleway,sans-serif;font-weight:300;font-size:21px;line-height:1.1;color:var(--mid-blue);white-space:nowrap}
.repair__title b{font-weight:300;color:var(--brand-blue)}
.repair__list{position:absolute;left:70px;top:290px;width:290px}
.repair__list li{margin-bottom:5.5px}
.contact{position:absolute;left:363px;top:243px;width:164px;height:253px}
.contact svg{position:absolute;left:0;top:0}
.contact .brand{position:absolute;left:28px;top:52px}
.contact .brand__name{font-size:13px;color:var(--white)}
.contact .brand__dot{width:13px;height:13px;background:var(--white)}
.contact__title{position:absolute;left:0;top:110px;width:164px;text-align:center;font-family:Raleway,sans-serif;font-weight:600;font-size:14.5px;color:var(--white)}
.contact__info{position:absolute;left:0;top:138px;width:164px;text-align:center;font-size:6.6px;line-height:1.6;color:var(--ice)}

.inside__bar{position:absolute;left:0;top:530px;width:799px;height:33px;background:var(--bar);color:#ddd;font-size:7px}
.inside__bar .brand{position:absolute;left:8px;top:9px}
.inside__bar .brand__name{font-size:11px;color:var(--white)}
.inside__bar .brand__dot{width:11px;height:11px;background:var(--white)}
.inside__url{position:absolute;left:170px;top:12px}
</style>
</head>
<body>

<section class="spread spread--outside">

  <article class="panel panel--why">
    <div class="photo why__photo" role="img" aria-label="Photo of a rock waterfall pool in a desert backyard"></div>
    <div class="why__card"></div>
    <h2 class="why__title"><b>WHY</b> CHOOSE US?</h2>
    <p class="why__intro">Thank you for the opportunity for our company to become your pool service provider! We’re committed to providing the best customer service possible! At the end of the day you want your pool to be clean, clear, operational, and for your service provider to be available when you need them!</p>
    <ul class="ticks why__list">
      <li>We’re licensed with the Desert State Builders Licensing Office, Bonded, and Fully Insured.</li>
      <li>A+ reviews with the Fair Trade Merchants Council, Marlo's Roster, Vetchly, Ornu, Chatterbook, and Searchly!</li>
      <li>All technicians are employees... not sub-contractors! Our employees are hard working, dependable, professional, and expected to follow our strict protocol for servicing your pool.</li>
      <li>Flat-fee service rates! Any additional equipment repairs, maintenance, or chemical implementations are directly authorized by you!</li>
      <li>No contracts! Our Service Level Agreement Form allows you to select your desired level of authorization for equipment repairs, filter maintenance, and extra chemical implementation programs.</li>
      <li>Our uniformed technicians arrive in distinctive, clean GPS-tracked company trucks.</li>
      <li>We leave detailed service slips after each service visit. In addition, all service visit information is electronically recorded and stored.</li>
      <li>Easy, online account management to view and pay invoices or authorize estimates.</li>
      <li>Invoices, estimates, questions, pictures, and video are communicated via e-mail!</li>
      <li>Free service calls to diagnose equipment issues outside of our normal service. 10% Service Client Discount for all repairs and replacement items.</li>
      <li>Tidewell Aqua Service knows the importance of communication! We’re available by phone, email, or text all days of the week.</li>
    </ul>
    <div class="partners" aria-label="Partner badges">
      <span class="partner partner--a"></span>
      <span class="partner partner--b"></span>
      <span class="partner partner--c"></span>
      <span class="partner partner--d"></span>
    </div>
    <div class="why__foot">
      <div class="brand"><span class="brand__dot" style="width:16px;height:16px"></span><span class="brand__name" style="font-size:15px">tidewellaqua</span></div>
    </div>
  </article>

  <article class="panel panel--cover-mid">
    <svg width="266" height="552" viewBox="0 0 266 552">
      <rect width="266" height="552" fill="#6787b3"/>
      <polygon points="16,0 249,0 249,310 16,430" fill="#8aa2b4" role="img" aria-label="Photo of grey pool steps with small turtle tiles"/>
      <polygon points="16,0 112,0 16,108" fill="#dfe7f0"/>
      <polygon points="16,432 249,312 249,524 16,524" fill="#ffffff"/>
    </svg>
    <div class="mid__brand">
      <div class="brand"><span class="brand__dot" style="width:22px;height:22px"></span><span class="brand__name" style="font-size:21px">tidewellaqua</span></div>
      <div class="brand__tag" style="margin-left:92px">Every Wave Stays Bright</div>
    </div>
    <div class="office">
      <div class="office__row"><strong>OFFICE/RETAIL LOCATION</strong><span>: 41762 E. KETTLE LN. #7</span></div>
      <div class="office__city">PHOENIX, ARIZONA 85000</div>
      <div class="office__grid">
        <b>Toll-Free</b><span>: 1.800.555.0162</span><b>Phoenix</b><span>: 480.555.0147</span>
        <b>Fax</b><span>: 480.555.0193</span><b>Scottsdale</b><span>: 480.555.0178</span>
      </div>
      <div class="office__web">www.tidewellaqua.com</div>
    </div>
  </article>

  <article class="panel panel--front">
    <div class="photo front__people" role="img" aria-label="Photo of a smiling family of three"></div>
    <div class="front__brand">
      <div class="brand"><span class="brand__dot"></span><span class="brand__name">tidewellaqua</span></div>
      <div class="brand__tag" style="margin-left:110px">Every Wave Stays Bright</div>
    </div>
    <p class="front__tagline">SERVICE - REPAIR - RENOVATION</p>
    <div class="photo front__pool" role="img" aria-label="Photo of a backyard pool with rock waterfall and flowers"></div>
    <div class="front__bar">
      <p>tidewellaqua.com<br>service@tidewellaqua.com</p>
      <p><span class="social"><i></i>Like Us On Chatterbook</span><span class="social"><i></i>&amp; Searchly Circle</span></p>
    </div>
  </article>
</section>

<section class="spread spread--inside">

  <article class="panel panel--about">
    <h2 class="section-title about__title">About <b>Us</b></h2>
    <div class="about__text">
      <p>A native to Phoenix, Darren Whitcombe founded Tidewell Aqua Service in 2000. Our company was built from the ground up by way of hard work, word of mouth, and determination. Our company will always remain firmly grounded, and continue to develop systems that put our customers first!</p>
      <p>Our philosophy is to treat every pool as if it were our own, run an efficient and organized business, and care for our employees.</p>
      <p>Tidewell Aqua Service is a yearly, proud contributor to the Saguaro Youth Medical Center Splash Smart Day. Please educate and watch all children around water... every accident can be avoided.</p>
    </div>
    <div class="snap snap--a" role="img" aria-label="Photo of a mosaic-tiled pool edge"></div>
    <div class="snap snap--b" role="img" aria-label="Photo of a pool with a desert mountain view"></div>
    <h2 class="section-title method__title">Our <b>Methodology</b></h2>
    <p class="method__lead">We believe in 5 important factors in maintaining a clean, clear, and operational pool...</p>
    <ul class="ticks method__list">
      <li>Good, Clean Water! Our local water supply contains high amounts of minerals. Pool chemicals add to this problem in a short amount of time. Our philosophy is to use the least amount of chemicals possible to achieve optimal water balance.</li>
      <li>Efficient Water Flow! The invention of variable-speed pumps has enabled the ability to "dial in" proper water flow... while driving down energy costs.</li>
      <li>Proper Filtration! Today’s high-capacity cartridge filters provide great filtration, save on wasted water from backwashing sand filters, and eliminate the need for water flow-restricting backwash valves.</li>
      <li>Functioning Cleaning System! Having a working automatic cleaning system is vital in keeping the pool surface clean of debris and dirt... and free of staining.</li>
      <li>A Dependable And Professional Pool Maintenance Technician! Our job is to not only oversee all of the items listed above... but to make sure your pool is in the best condition possible!</li>
    </ul>
  </article>

  <article class="panel panel--repair">
    <div class="photo repair__hero" role="img" aria-label="Photo of a resort-style pool with rock waterfall, palms and mist"></div>
    <div class="snap snap--c" role="img" aria-label="Photo of a pool and spa with desert landscaping"></div>
    <div class="snap snap--d" role="img" aria-label="Photo of a stone water feature spilling into a pool"></div>
    <div class="snap snap--e" role="img" aria-label="Photo of a bright blue backyard pool"></div>
    <h2 class="repair__title"><b>Equipment Repair</b><br>&amp; Installation</h2>
    <ul class="ticks repair__list">
      <li>We’re educated on all phases of swimming pool equipment repair and installation... with a focus on energy-efficiency and optimum performance!</li>
      <li>We’re an KVE &amp; BTU Authorized Installer of variable-speed pool pumps. KVE &amp; BTU trust us to properly install and calibrate all variable-speed pumps. We've been equipped to handle the new industry standards on variable-speed pumps since Arizona law went into effect January 1st, 2011.</li>
      <li>We’re experts at acid washes and erasing the mineral build-up off of waterlines. All work is done in-house with our customized cleaning rig and trailer.</li>
      <li>Heating systems. New efficiency standards have made installation and operation more affordable than ever.<br>Remote control automation systems. Technology now allows the user to easily view and control their entire pool system via a remote home computer, tablet, or phone!</li>
      <li>Brilliant, color-changing LED lighting for pools and spas! The benefits of LED include brighter and broader displays... while lasting much longer than your typical light bulbs.</li>
      <li>Salt systems provide a soft-water experience! In addition to the benefit of better feeling water, salt systems generate plenty of chlorine to keep your pool sanitized.</li>
    </ul>
    <div class="contact">
      <svg width="164" height="253" viewBox="0 0 164 253" aria-hidden="true">
        <polygon points="0,0 164,0 164,218 82,253 0,218" fill="#3f6ea8"/>
        <polygon points="6,6 158,6 158,92 6,92" fill="#5b86bb" opacity=".35"/>
      </svg>
      <div class="brand"><span class="brand__dot"></span><span class="brand__name">tidewellaqua</span></div>
      <h2 class="contact__title">CONTACT US</h2>
      <p class="contact__info">Office: 480-555-0147<br>Fax: 480-555-0193<br>Email: service@tidewellaqua.com<br>tidewellaqua.com</p>
    </div>
  </article>

  <footer class="inside__bar">
    <div class="brand"><span class="brand__dot"></span><span class="brand__name">tidewellaqua</span></div>
    <span class="inside__url">www.http://tidewellaqua.com</span>
  </footer>
</section>

</body>
</html>
```